Wordpress Design for a Private Label BBQ Brand

For our new brand, we'd need a new Wordpress website. We'd prefer to run the website on Wordpress

We'd like to include the following
- space for description of the brand
- space for product portfolio (not a shop!)
- space for socials
- space for support
- space for contact

```html
<!DOCTYPE html>
<html lang="en">
<head>
<meta charset="utf-8">
<title>Braciera — Private Label BBQ Brand</title>
<link href="https://fonts.googleapis.com/css2?family=Libre+Baskerville:wght@700&family=Lato:wght@400;700&display=swap" rel="stylesheet">
<style>
:root{
  --red:#d9261c;
  --red-deep:#c0192a;
  --orange:#ee6a24;
  --orange-soft:#ef7a2c;
  --blue-a:#2f56a8;
  --blue-b:#3f86c6;
  --ink:#222;
  --muted:#555;
  --white:#fff;
  --rule:#d8d8d8;
}
*{margin:0;padding:0;box-sizing:border-box}
html,body{width:1200px;height:4024px;overflow:hidden;background:var(--white)}
body{position:relative;font-family:'Lato',sans-serif;color:var(--ink)}
.abs{position:absolute}
.serif{font-family:'Libre Baskerville',serif;font-weight:700}
.center{left:0;width:1200px;text-align:center}

/* hero */
.hero{top:0;left:0;width:1200px;height:719px;background:radial-gradient(ellipse at 55% 60%,#7a3214 0%,#3b2a1c 35%,#1d2a22 70%,#17201c 100%)}
.brand{font-family:'Libre Baskerville',serif;font-weight:700;color:var(--white);display:flex;align-items:center;gap:10px}
.brand .dot{width:22px;height:22px;border-radius:50%;background:var(--red)}
.nav{top:60px;left:434px;display:flex;gap:22px;font-size:17px;font-weight:700;color:var(--white)}
.nav .on{color:var(--orange)}
.login{top:62px;left:925px;font-size:14px;color:var(--white);display:flex;gap:16px;align-items:center}
.btn{background:linear-gradient(90deg,var(--red-deep),var(--orange));color:var(--white);font-weight:700;border-radius:34px;display:flex;align-items:center;justify-content:center}

/* about */
.about{top:719px;left:0;width:1200px;height:643px;background:linear-gradient(90deg,var(--blue-a),var(--blue-b))}
.eyebrow{font-size:20px;font-weight:700;letter-spacing:.2px}
/* products */
.card{top:1553px;width:312px;height:355px}
.card .ph{height:292px}
.card .lab{height:63px;display:flex;justify-content:space-between;align-items:center;padding:0 20px;color:var(--white);font-size:21px;font-weight:700}
/* benefits */
.benefits{top:1992px;left:0;width:1200px;height:844px;background:linear-gradient(90deg,var(--red-deep),var(--orange));overflow:hidden}
.feat{font-size:18px;color:var(--white);line-height:1.4}
.bub{width:156px;height:156px;border-radius:50%;background:radial-gradient(circle at 40% 40%,#4a4a4a,#151515)}
/* support */
.sup{top:3044px;width:196px;height:195px;text-align:center;font-size:20px;font-weight:700;color:#444}
.sup svg{display:block;margin:30px auto 14px}
.div{top:3044px;width:1px;height:195px;background:var(--rule)}
/* join */
.join{top:3297px;left:0;width:1200px;height:370px;background:radial-gradient(ellipse at 55% 65%,#b2461a 0%,#5a2812 45%,#1e140f 100%)}
.social{width:48px;height:48px;border-radius:50%;background:var(--white)}
/* footer */
.flink{font-size:15px;color:var(--muted)}
</style>
</head>
<body>

<!-- hero -->
<section class="abs hero" role="img" aria-label="Charcoal kettle grill with glowing embers and flying sparks"></section>
<div class="abs brand" style="top:44px;left:111px;font-size:38px"><span class="dot"></span>BRACIERA</div>
<nav class="abs nav"><span class="on">Home</span><span>About</span><span>Products</span><span>Support</span><span>Contact</span></nav>
<div class="abs login">
  <svg width="18" height="18" viewBox="0 0 18 18"><circle cx="7.5" cy="7.5" r="5.5" fill="none" stroke="#fff" stroke-width="2.4"/><line x1="11.5" y1="11.5" x2="16" y2="16" stroke="#fff" stroke-width="2.6"/></svg>
  <span style="display:flex;gap:8px;align-items:center"><svg width="12" height="15" viewBox="0 0 12 15"><circle cx="6" cy="4" r="3.5" fill="#fff"/><path d="M0 15c0-5 2.5-7 6-7s6 2 6 7z" fill="#fff"/></svg>Login/Sign up</span>
</div>
<div class="abs center" style="top:162px;font-size:21px;color:#fff">BRACIERA</div>
<h1 class="abs center serif" style="top:215px;font-size:56px;color:#fff">PRIVATE LABEL BBQ BRAND</h1>
<div class="abs btn" style="top:316px;left:470px;width:260px;height:67px;font-size:19px">EXPLORE PRODUCTS</div>

<!-- about -->
<section class="abs about"></section>
<div class="abs eyebrow" style="top:800px;left:111px;color:#fff">ABOUT US</div>
<h2 class="abs serif" style="top:842px;left:111px;font-size:42px;line-height:52px;color:#fff">WELCOME TO<br>BRACIERA</h2>
<p class="abs" style="top:970px;left:111px;width:395px;font-size:15.5px;line-height:26px;color:#fff">Lorem ipsum dolor sit amet, consectetur adipiscing elit, sed do eiusmod tempor incididunt ut labore et dolore magna aliqua. Ut enim ad minim veniam, quis nostrud exercitation ullamco laboris nisi ut aliquip ex ea commodo consequat. Duis aute irure dolor in reprehenderit in voluptate velit.</p>
<div class="abs" style="top:1165px;left:111px;display:flex;align-items:center;gap:20px;color:#fff;font-size:18px;font-weight:700">
  <svg width="60" height="60" viewBox="0 0 60 60"><defs><linearGradient id="pg" x1="0" x2="1"><stop offset="0" stop-color="#c0192a"/><stop offset="1" stop-color="#ee6a24"/></linearGradient></defs><circle cx="30" cy="30" r="30" fill="url(#pg)"/><path d="M23 18v24l20-12z" fill="#fff"/></svg>
  WATCH VIDEO
</div>
<div class="abs" role="img" aria-label="Close-up of flames over a grill grate with corn" style="top:791px;left:692px;width:449px;height:467px;background:radial-gradient(circle at 60% 50%,#f2a23a,#a8450f 45%,#2a1408 85%)"></div>
<div class="abs" role="img" aria-label="Black ceramic kamado grill on a metal stand" style="top:898px;left:516px;width:296px;height:446px;background:radial-gradient(ellipse at 50% 40%,#3a3a3a,#111 60%,rgba(17,17,17,0) 72%)"></div>

<!-- products -->
<div class="abs center" style="top:1426px;font-size:21px;color:var(--red)">COLLECTION</div>
<h2 class="abs center serif" style="top:1470px;font-size:40px">OUR PRODUCTS</h2>
<div class="abs card" style="left:111px"><div class="ph" role="img" aria-label="Four detail views of a black ceramic grill" style="background:linear-gradient(135deg,#2b2b2b,#6b5a45 50%,#1c1c1c)"></div><div class="lab" style="background:#a9b8d4"><span>Barbecue Grills</span><span>⟶</span></div></div>
<div class="abs card" style="left:444px"><div class="ph" role="img" aria-label="Stainless steel barbecue tool set in an aluminium case" style="background:linear-gradient(135deg,#d9d9d9,#3a3a3a 40%,#9a9a9a)"></div><div class="lab" style="background:#e9b08a"><span>Barbecue Accessories</span><span>⟶</span></div></div>
<div class="abs card" style="left:777px"><div class="ph" role="img" aria-label="Grill with tool set as a gift package" style="background:linear-gradient(135deg,#efefef,#c9c9c9 50%,#efefef)"></div><div class="lab" style="background:#a9b8d4"><span>Combo Gift Packages</span><span>⟶</span></div></div>

<!-- benefits -->
<section class="abs benefits">
  <div class="abs" style="left:92px;top:336px;width:1016px;height:1016px;border-radius:50%;background:var(--orange-soft)"></div>
  <div class="abs" style="left:405px;top:465px;width:390px;height:390px;border-radius:50%;background:#fff"></div>
</section>
<div class="abs center" style="top:2056px;font-size:21px;color:#fff">BENEFITS</div>
<h2 class="abs center serif" style="top:2100px;font-size:40px;color:#fff">WHY CHOOSE BRACIERA</h2>
<div class="abs center feat" style="top:2185px">Bottom damper to control airflow<br>for precise temperature control</div>
<div class="abs" role="img" aria-label="Kamado grill front view" style="top:2485px;left:480px;width:240px;height:350px;background:radial-gradient(ellipse at 50% 45%,#3b3b3b,#141414 60%,rgba(255,255,255,0) 72%)"></div>
<div class="abs bub" role="img" aria-label="Bottom damper detail" style="top:2250px;left:522px"></div>
<div class="abs bub" role="img" aria-label="Top damper detail" style="top:2308px;left:335px"></div>
<div class="abs bub" role="img" aria-label="Textured ceramic surface" style="top:2308px;left:708px"></div>
<div class="abs bub" role="img" aria-label="Lid thermometer" style="top:2461px;left:213px"></div>
<div class="abs bub" role="img" aria-label="Iron hinge detail" style="top:2461px;left:831px"></div>
<div class="abs bub" role="img" aria-label="Insulated handle detail" style="top:2652px;left:203px"></div>
<div class="abs bub" role="img" aria-label="Steel cart with casters" style="top:2652px;left:841px;background:radial-gradient(circle,#f2f2f2,#cfcfcf)"></div>
<div class="abs feat" style="top:2348px;left:90px;width:230px;text-align:right">Adjustable top damper<br>maintains airflow</div>
<div class="abs feat" style="top:2348px;left:883px">Stripes designed to<br>increase beauty</div>
<div class="abs feat" style="top:2484px;left:30px;width:168px;text-align:right">You can see how the temperature changes from the thermometer</div>
<div class="abs feat" style="top:2500px;left:1006px">Preminun hinge<br>Material - Iron</div>
<div class="abs feat" style="top:2703px;left:40px;width:142px;text-align:right">Heat insulation<br>handle</div>
<div class="abs feat" style="top:2673px;left:1015px;width:140px">Stainless steel mobile cart with locking casters</div>

<!-- support -->
<div class="abs center" style="top:2919px;font-size:21px;color:var(--red)">HELP</div>
<h2 class="abs center serif" style="top:2962px;font-size:40px">SUPPORT</h2>
<div class="abs sup" style="left:111px"><svg width="64" height="72" viewBox="0 0 64 72" fill="none" stroke="#d9261c" stroke-width="3"><path d="M18 4c-4 5 4 7 0 12M32 4c-4 5 4 7 0 12M46 4c-4 5 4 7 0 12"/><path d="M6 24h52c0 14-12 22-26 22S6 38 6 24z"/><path d="M20 44 10 68M44 44l10 16"/><circle cx="54" cy="64" r="5"/></svg>Grill Skills</div>
<div class="abs div" style="left:306px"></div>
<div class="abs sup" style="left:307px"><svg width="64" height="72" viewBox="0 0 64 72" fill="none" stroke="#d9261c" stroke-width="3"><path d="M8 14h40v54H8z"/><path d="M14 8h40v54"/><path d="M16 58 34 24l10 6-18 32z"/><path d="M16 28h14M16 36h10"/></svg>Manuals</div>
<div class="abs div" style="left:502px"></div>
<div class="abs sup" style="left:503px"><svg width="80" height="72" viewBox="0 0 80 72" fill="none" stroke="#d9261c" stroke-width="4"><path d="M20 28h54M62 16l12 12-12 12"/><path d="M60 48H6M18 36 6 48l12 12"/></svg>Replacement<br>Parts</div>
<div class="abs div" style="left:697px"></div>
<div class="abs sup" style="left:698px"><svg width="80" height="72" viewBox="0 0 80 72" fill="none" stroke="#d9261c" stroke-width="3"><rect x="4" y="4" width="52" height="40" rx="10"/><path d="M16 44v14l12-14"/><path d="M56 20h10a10 10 0 0 1 10 10v14a10 10 0 0 1-10 10h-4v12L50 54H38"/><path d="M24 18a6 6 0 1 1 8 6v6"/><circle cx="30" cy="37" r="1.5"/></svg>FAQs</div>
<div class="abs div" style="left:892px"></div>
<div class="abs sup" style="left:893px"><svg width="80" height="72" viewBox="0 0 80 72" fill="none" stroke="#d9261c" stroke-width="3"><path d="M4 14 24 6l28 8 24-8v52l-24 8-28-8-20 8z"/><path d="M24 6v52M52 14v52"/><path d="M12 30l6 6M18 30l-6 6M34 24h10v12h-8v12M60 40l8-8"/></svg>Schematics</div>

<!-- join -->
<section class="abs join" role="img" aria-label="Flames rising from a barbecue grate"></section>
<div class="abs center" style="top:3356px;font-size:21px;color:#fff">JOIN US</div>
<h2 class="abs center serif" style="top:3400px;font-size:40px;color:#fff">JOIN OUR COMMUNITY</h2>
<div class="abs" style="top:3480px;left:111px;font-size:18px;font-weight:700;color:#fff">Email updates from our community</div>
<div class="abs" style="top:3517px;left:111px;width:362px;height:61px;background:#fff;border-radius:8px 0 0 8px;font-size:16px;color:#444;padding:20px 22px">Email Address</div>
<div class="abs" style="top:3517px;left:473px;width:129px;height:61px;background:var(--red);border-radius:0 8px 8px 0;color:#fff;font-size:18px;font-weight:700;display:flex;align-items:center;justify-content:center">SUBSCRIBE</div>
<div class="abs" style="top:3480px;left:692px;font-size:18px;font-weight:700;color:#fff">Social</div>
<div class="abs social" aria-label="Social channel one" style="top:3518px;left:692px"></div>
<div class="abs social" aria-label="Social channel two" style="top:3518px;left:745px"></div>
<div class="abs social" aria-label="Social channel three" style="top:3518px;left:799px"></div>
<div class="abs social" aria-label="Social channel four" style="top:3518px;left:854px"></div>

<!-- footer -->
<div class="abs brand" style="top:3750px;left:111px;font-size:52px;color:var(--ink)"><span class="dot" style="width:30px;height:30px"></span>BRACIERA</div>
<div class="abs" style="top:3734px;left:533px;font-size:18px;font-weight:700">Quick Links</div>
<div class="abs flink" style="top:3774px;left:533px;line-height:26.5px">Home<br>About<br>Products<br>Support<br>Contact</div>
<div class="abs" style="top:3734px;left:722px;font-size:18px;font-weight:700">Contact Us</div>
<svg class="abs" style="top:3774px;left:722px" width="12" height="16" viewBox="0 0 12 16"><path d="M6 0a6 6 0 0 1 6 6c0 4-6 10-6 10S0 10 0 6a6 6 0 0 1 6-6z" fill="#d9261c"/><circle cx="6" cy="6" r="2.2" fill="#fff"/></svg>
<div class="abs flink" style="top:3774px;left:756px;line-height:20px">No: 123emo enim ipsam volupta<br>tem quia voluptas sit aspe</div>
<svg class="abs" style="top:3837px;left:722px" width="14" height="14" viewBox="0 0 14 14"><path d="M3 0l3 3-2 2c1 2 3 4 5 5l2-2 3 3-2 3C6 14 0 8 0 3z" fill="#d9261c"/></svg>
<div class="abs flink" style="top:3835px;left:756px">1 888 888 8888</div>
<svg class="abs" style="top:3878px;left:722px" width="16" height="12" viewBox="0 0 16 12"><rect width="16" height="12" rx="1" fill="#d9261c"/><path d="M1 1l7 6 7-6" fill="none" stroke="#fff" stroke-width="1.5"/></svg>
<div class="abs flink" style="top:3876px;left:756px">info@braciera.com</div>
<div class="abs" style="top:3933px;left:111px;width:978px;height:1px;background:var(--rule)"></div>
<div class="abs center flink" style="top:3963px">© 2023, Braciera. All Rights Reserved. Privacy Policy |&nbsp; Terms &amp; Conditions</div>

</body>
</html>
```